Young Entrepreneur needs the sexiest, slickest, hottest ANDROID ALARM APP DESIGN.

Now that I have your attention...

The name of the Application is BrimNote, using 'Stickers' this application is meant to get you to do what you need to do AND TO DO IT NOW, with a UI so simple my grandma can use it.

Using the provided sketches as a REFERENCE point, THREE (3) SCREENS will be needed, including a couple of design accents, which when the project is completed will be sent directly to a programming team.

Industry/Entity Type

Android

Requirements
Must have
• Creativity in simplicity. but please, go wild, do your 'thang'... Just keep it simple and clean.

```html
<!DOCTYPE html>
<html lang="en">
<head>
<meta charset="utf-8">
<title>BrimNote – Alarm Stickers</title>
<link rel="stylesheet" href="https://fonts.googleapis.com/css2?family=Open+Sans:wght@300;400;600;700&display=swap">
<style>
  :root {
    --screen-edge: #2b97cf;
    --screen-glow: #6cc0e2;
    --line: rgba(255, 255, 255, 0.92);
    --sticker-fill: rgba(255, 255, 255, 0.06);
    --sticker-gloss: rgba(255, 255, 255, 0.13);
    --text: #ffffff;
    --brand: #e9f4fa;
  }
  * { margin: 0; padding: 0; box-sizing: border-box; }
  html, body {
    width: 787px;
    height: 1200px;
    overflow: hidden;
  }
  body {
    font-family: "Open Sans", sans-serif;
    color: var(--text);
  }
  .app-screen {
    position: relative;
    width: 787px;
    height: 1200px;
    background: radial-gradient(ellipse 62% 48% at 50% 44%, var(--screen-glow) 0%, #4aaed9 45%, var(--screen-edge) 100%);
  }
  .sticker-defs { position: absolute; width: 0; height: 0; }
  .sticker {
    position: absolute;
    width: 170px;
    height: 170px;
    transform: translate(-50%, -50%);
  }
  .sticker-shape {
    position: absolute;
    inset: 0;
    width: 170px;
    height: 170px;
  }
  .sticker-content {
    position: absolute;
    inset: 0;
    display: flex;
    flex-direction: column;
    align-items: center;
    justify-content: center;
    padding-top: 4px;
  }
  .sticker-time {
    font-weight: 700;
    font-size: 47px;
    line-height: 1;
    letter-spacing: -1px;
  }
  .sticker-label {
    font-weight: 300;
    font-size: 24px;
    line-height: 1.2;
    margin-top: 3px;
  }
  .sticker-period {
    position: absolute;
    top: 32px;
    right: 34px;
    font-size: 11px;
    font-weight: 400;
  }
  .sticker-add-icon {
    position: absolute;
    inset: 0;
    margin: auto;
    width: 58px;
    height: 58px;
  }
  .set-alarms {
    position: absolute;
    left: 233px;
    top: 967px;
    width: 328px;
    height: 66px;
    border: 2px solid var(--line);
    background: transparent;
    color: var(--text);
    font-family: "Open Sans", sans-serif;
    font-weight: 300;
    font-size: 36px;
    display: flex;
    align-items: center;
    justify-content: center;
  }
  .brand-name {
    position: absolute;
    left: 0;
    right: 0;
    top: 1106px;
    text-align: center;
    font-weight: 700;
    font-size: 30px;
    color: var(--brand);
  }
</style>
</head>
<body>
<main class="app-screen">
  <svg class="sticker-defs" aria-hidden="true">
    <defs>
      <clipPath id="decagon-clip">
        <polygon points="169,85 153,134.4 111,164.9 59,164.9 17,134.4 1,85 17,35.6 59,5.1 111,5.1 153,35.6"/>
      </clipPath>
      <symbol id="decagon" viewBox="0 0 170 170">
        <polygon points="169,85 153,134.4 111,164.9 59,164.9 17,134.4 1,85 17,35.6 59,5.1 111,5.1 153,35.6" fill="var(--sticker-fill)"/>
        <polygon points="78,0 170,0 170,150" fill="var(--sticker-gloss)" clip-path="url(#decagon-clip)"/>
        <polygon points="169,85 153,134.4 111,164.9 59,164.9 17,134.4 1,85 17,35.6 59,5.1 111,5.1 153,35.6" fill="none" stroke="var(--line)" stroke-width="2"/>
      </symbol>
    </defs>
  </svg>

  <!-- Row 1 -->
  <div class="sticker" style="left:171px; top:165px;">
    <svg class="sticker-shape"><use href="#decagon"/></svg>
    <span class="sticker-period">am</span>
    <div class="sticker-content"><span class="sticker-time">6:40</span><span class="sticker-label">Shower</span></div>
  </div>
  <div class="sticker" style="left:395px; top:165px;">
    <svg class="sticker-shape"><use href="#decagon"/></svg>
    <span class="sticker-period">pm</span>
    <div class="sticker-content"><span class="sticker-time">15:00</span><span class="sticker-label">Date</span></div>
  </div>
  <div class="sticker sticker-add" style="left:618px; top:165px;" aria-label="Add alarm">
    <svg class="sticker-shape"><use href="#decagon"/></svg>
    <svg class="sticker-add-icon" viewBox="0 0 58 58"><path d="M29 2v54M2 29h54" stroke="#fff" stroke-width="8"/></svg>
  </div>

  <!-- Row 2 -->
  <div class="sticker" style="left:171px; top:362px;">
    <svg class="sticker-shape"><use href="#decagon"/></svg>
    <span class="sticker-period">am</span>
    <div class="sticker-content"><span class="sticker-time">6:40</span><span class="sticker-label">Shower</span></div>
  </div>
  <div class="sticker" style="left:395px; top:362px;">
    <svg class="sticker-shape"><use href="#decagon"/></svg>
    <span class="sticker-period">pm</span>
    <div class="sticker-content"><span class="sticker-time">15:00</span><span class="sticker-label">Date</span></div>
  </div>
  <div class="sticker" style="left:618px; top:362px;">
    <svg class="sticker-shape"><use href="#decagon"/></svg>
    <span class="sticker-period">pm</span>
    <div class="sticker-content"><span class="sticker-time">20:00</span><span class="sticker-label">Play-offs</span></div>
  </div>

  <!-- Row 3 -->
  <div class="sticker" style="left:171px; top:559px;">
    <svg class="sticker-shape"><use href="#decagon"/></svg>
    <span class="sticker-period">am</span>
    <div class="sticker-content"><span class="sticker-time">6:40</span><span class="sticker-label">Shower</span></div>
  </div>
  <div class="sticker" style="left:395px; top:559px;">
    <svg class="sticker-shape"><use href="#decagon"/></svg>
    <span class="sticker-period">pm</span>
    <div class="sticker-content"><span class="sticker-time">15:00</span><span class="sticker-label">Date</span></div>
  </div>
  <div class="sticker" style="left:618px; top:559px;">
    <svg class="sticker-shape"><use href="#decagon"/></svg>
    <span class="sticker-period">pm</span>
    <div class="sticker-content"><span class="sticker-time">20:00</span><span class="sticker-label">Play-offs</span></div>
  </div>

  <!-- Row 4 -->
  <div class="sticker" style="left:171px; top:756px;">
    <svg class="sticker-shape"><use href="#decagon"/></svg>
    <span class="sticker-period">am</span>
    <div class="sticker-content"><span class="sticker-time">6:40</span><span class="sticker-label">Shower</span></div>
  </div>
  <div class="sticker" style="left:395px; top:756px;">
    <svg class="sticker-shape"><use href="#decagon"/></svg>
    <span class="sticker-period">pm</span>
    <div class="sticker-content"><span class="sticker-time">15:00</span><span class="sticker-label">Date</span></div>
  </div>
  <div class="sticker" style="left:618px; top:756px;">
    <svg class="sticker-shape"><use href="#decagon"/></svg>
    <span class="sticker-period">pm</span>
    <div class="sticker-content"><span class="sticker-time">20:00</span><span class="sticker-label">Play-offs</span></div>
  </div>

  <div class="set-alarms">Set Alarms</div>

  <div class="brand-name">BrimNote</div>
</main>
</body>
</html>
```